Web Design For Coral Basin Pool Service

We are working with a company that wants a website for their pool service. Some sites to use for content/competitors and inspiration:
https://sacramento.lumawaterworks.example/builder/newbuild/repair/ppc
https://orchardsplashcareplus.example/
https://bluefinaquacare.example/
https://www.halvorsenplasterworks.example/pool-renovation-ga/
Thank you for taking the time to consider designing a website for us. We are web developers based in Stockton, CA, USA. Most of our projects go through the same process. Understanding this process may help you win a project with us. We custom-code all of our websites in-house. We don’t have any requirements as to what tools you use for your design, but we prefer Figma files. For any design that we label as four-stars, we send it to the client for review. The client picks the final design they want us to use. Once we complete this process, we will continue to show additional clients all the four-star sites and purchase them later. Your designs will have multiple chances to sell. For better chances of success, we ask that you follow these guidelines.
IMAGES:
If you use any images or icons in the design, we ask that you have a link to the asset so we can purchase the image/icon. Most of the designs we submit do not have the customer’s images on them unless they have some great images. Be creative; show us the feeling you are trying to portray with your image choices. Use any royalty-free site you choose. We subscribe to Adobe and mainly use their images, but we can purchase images outside of Adobe. PLEASE NOTE: we will not submit designs to clients with watermarks on the images.
FONTS:
We ask that you identify the fonts used in the design. This can be done in a message if you want. We typically use Google Fonts and Adobe Fonts.
CONTENT:
We're always open to different content and ideas. We often submit designs with stock images so the client can see our vision. We typically take pictures after the website launch to use their images with our vision. Lorem Ipsum is fine for paragraphs, but we ask that you write the headers in correct English. We want to be able to show the vision and identify the sections of the website.
INSPIRATION:
We typically add a couple of links in the brief of websites we like to help you get started in your design.
REVISIONS:
We do not often ask for revisions of the designs unless we see something in the design that may not appeal to the client. If there are slight changes that we want to make, we do that in the development process.
FEEDBACK:
We rarely give feedback on designs during the design process. We are working on many website projects and do not have the time to provide feedback. We usually respond if your request is well thought out and asks specific questions, but a note asking “feedback, please” usually goes unanswered.

```html
<!DOCTYPE html>
<html lang="en">
<head>
<meta charset="utf-8">
<title>Coral Basin Pool Service</title>
<link href="https://fonts.googleapis.com/css2?family=Lato:wght@300;400;700&family=Tinos:wght@400;700&display=swap" rel="stylesheet">
<style>
:root{
  --blue:#2a9cf3;
  --blue-dark:#1d84d8;
  --ink:#4b4b4b;
  --text:#5e5e5e;
  --white:#ffffff;
  --grey:#7b7b7b;
  --night:#0c1826;
  --serif:'Tinos', 'Times New Roman', serif;
  --sans:'Lato', Arial, sans-serif;
}
*{margin:0;padding:0;box-sizing:border-box}
html,body{width:1200px;height:4721px;overflow:hidden;background:var(--white);font-family:var(--sans);color:var(--text)}
.page{position:relative;width:1200px;height:4721px;overflow:hidden}
.abs{position:absolute}
.center{text-align:center}
.section-title{font-family:var(--serif);font-weight:700;font-size:50px;color:var(--ink);letter-spacing:1px}
.btn{position:absolute;display:flex;align-items:center;justify-content:center;border-radius:20px;font-size:15px;font-weight:700;text-decoration:none}
.btn-blue{background:var(--blue);color:var(--white)}
.btn-white{background:var(--white);color:var(--blue)}
.photo{position:absolute}

/* header */
.site-header{top:0;left:0;width:1200px;height:128px;background:var(--white);border-top:5px solid #555}
.brand{left:114px;top:36px;color:var(--blue);font-family:var(--sans);font-weight:400;font-size:27px;line-height:30px;letter-spacing:2px;text-transform:uppercase}
.nav a{position:absolute;top:56px;font-size:14px;color:#6a6a6a;text-decoration:none}
.nav a.active{color:var(--blue)}
.call-icon{left:908px;top:40px;width:52px;height:52px;border-radius:50%;background:var(--blue)}
.call-label{left:969px;top:42px;font-size:15px;color:var(--blue)}
.call-number{left:969px;top:66px;font-size:15px;color:#555}

/* hero */
.hero{top:128px;left:0;width:1200px;height:735px}
.hero-photo{inset:0;background:linear-gradient(180deg,#2c4a4c 0%,#2b5f73 40%,#2a6e8c 70%,#2c7fa6 100%)}
.hero-welcome{top:225px;width:1200px;font-size:50px;font-weight:300;color:var(--white)}
.hero-title{top:300px;width:1200px;font-family:var(--serif);font-weight:700;font-size:76px;color:var(--white);letter-spacing:2px}

/* about */
.about-frame{left:112px;top:898px;width:432px;height:426px;background:linear-gradient(135deg,#3aa3e8,#1f7fcc)}
.about-photo{left:150px;top:933px;width:432px;height:428px;background:linear-gradient(160deg,#2aa0d8,#4fc1e6 55%,#8b5a3c 100%)}
.about-title{left:646px;top:880px}
.about-text{left:646px;top:970px;width:444px;font-size:14px;line-height:25.6px;color:#5a5a5a}
.about-text p+p{margin-top:26px}

/* services */
.services{top:1374px;left:0;width:1200px;height:1112px;background:linear-gradient(180deg,#2fa1f5,#2a95ec)}
.services-title{top:250px;width:1200px;color:var(--white)}
.services-intro{top:330px;left:250px;width:700px;font-size:14px;line-height:25px;color:var(--white)}
.card-photo{position:absolute;border:3px solid var(--white)}
.card-num{position:absolute;width:317px;font-size:40px;color:var(--white);font-weight:400}
.card-title{position:absolute;width:317px;font-family:var(--serif);font-weight:700;font-size:24px;color:var(--white)}
.card-text{position:absolute;width:260px;font-size:14px;line-height:25px;color:var(--white)}
.feature-card{left:440px;top:453px;width:318px;height:518px;background:var(--white)}

/* why */
.why{top:2486px;left:0;width:1200px;height:515px;background:linear-gradient(180deg,#7f7f7f,#767676)}
.why-title{top:125px;width:1200px;color:var(--white)}
.why-item{position:absolute;top:220px;width:240px;color:var(--white)}
.why-item svg{display:block;margin:0 auto}
.why-item h3{margin-top:30px;font-family:var(--serif);font-weight:700;font-size:24px}
.why-item p{margin-top:12px;font-size:14px;line-height:24px}

/* blog */
.blog-title{top:3135px;width:1200px}
.blog-card{position:absolute;top:3232px;width:305px}
.blog-photo{width:305px;height:245px;position:relative}
.blog-date{margin-top:30px;font-size:9px;color:var(--blue)}
.blog-card h3{margin-top:8px;font-family:var(--serif);font-weight:700;font-size:25px;color:#5a5a5a}
.blog-card p{margin-top:8px;font-size:14px;line-height:26px;color:#6a6a6a;padding:0 18px}
.blog-card a{display:inline-block;margin-top:10px;font-size:14px;color:var(--blue)}
.arrow{position:absolute;top:3337px;width:42px;height:42px;border-radius:50%;background:#000}

/* contact + footer */
.footer{top:3710px;left:0;width:1200px;height:1011px;background:linear-gradient(180deg,#13263a,#0b1724 40%,#0a1420)}
.contact-title{top:268px;width:1200px;color:var(--white)}
.field{position:absolute;width:474px;height:52px;background:var(--white);font-size:14px;color:#666;padding:18px 20px}
.foot-brand{left:114px;top:650px;color:var(--white);font-size:40px;line-height:46px;letter-spacing:3px;text-transform:uppercase;font-weight:400}
.foot-info{position:absolute;left:114px;font-size:14px;color:var(--white);display:flex;align-items:flex-start;gap:12px;line-height:22px}
.foot-col{position:absolute;top:655px;color:var(--white)}
.foot-col h4{font-family:var(--serif);font-weight:700;font-size:24px;margin-bottom:12px}
.foot-col a{display:block;font-size:14px;color:var(--white);text-decoration:none;line-height:34.6px;padding-left:4px}
.copyright{top:975px;width:1200px;font-size:14px;color:var(--white)}
</style>
</head>
<body>
<div class="page">

  <header class="site-header abs">
    <div class="brand abs">Coral Basin<br>Pool Service</div>
    <nav class="nav">
      <a class="active" href="#" style="left:425px">Home</a>
      <a href="#" style="left:508px">About Us</a>
      <a href="#" style="left:613px">Services</a>
      <a href="#" style="left:712px">Blog</a>
      <a href="#" style="left:783px">Contact Us</a>
    </nav>
    <div class="call-icon abs">
      <svg width="52" height="52" viewBox="0 0 52 52"><path d="M19 16c2-1 3 0 4 2l2 4c1 2 0 3-1 4l-1 1c1 3 4 6 7 7l1-1c1-1 2-2 4-1l4 2c2 1 3 2 2 4l-1 2c-2 3-6 3-10 1-5-3-9-7-12-12-2-4-2-8 1-10z" fill="#fff"/></svg>
    </div>
    <div class="call-label abs">Call Us</div>
    <div class="call-number abs">+1 888 888 8888</div>
  </header>

  <section class="hero abs">
    <div class="hero-photo photo" role="img" aria-label="Resort swimming pool with lounge chairs and palm trees at dusk"></div>
    <div class="hero-welcome abs center">Welcome To</div>
    <h1 class="hero-title abs center">CORAL BASIN POOL SERVICE</h1>
    <a class="btn btn-white" href="#" style="left:515px;top:416px;width:170px;height:37px;font-weight:400;font-size:15px">Contact Us</a>
    <svg class="abs" style="left:0;top:615px" width="1200" height="120" viewBox="0 0 1200 120" preserveAspectRatio="none">
      <path d="M0 20 Q600 200 1200 20 V120 H0Z" fill="var(--blue)"/>
      <path d="M0 62 Q600 180 1200 40 V120 H0Z" fill="#fff"/>
    </svg>
  </section>

  <section class="about">
    <div class="about-frame photo" role="img" aria-label="Pool water texture backdrop"></div>
    <div class="about-photo photo" role="img" aria-label="Technician lowering a robotic pool cleaner into a pool beside a skimmer net"></div>
    <h2 class="section-title about-title abs">About Us</h2>
    <div class="about-text abs">
      <p>Lorem ipsum dolor sit amet, consectetur adipiscing elit, sed do eiusmod tempor incididunt ut labore et dolore magna aliqua. Ut enim ad minim veniam, quis nostrud exercitation ullamco laboris nisi ut aliquip ex ea commodo consequat.</p>
      <p>Duis aute irure dolor in reprehenderit in voluptate velit esse cillum dolore eu fugiat nulla pariatur. Excepteur sint occaecat cupidatat non proident, sunt in culpa qui officia deserunt mollit anim id est laborum.Sed ut perspiciatis unde omnis iste natus error sit voluptatem accusantium doloremque laudantium, totam rem aperiam, eaque ipsa quae ab illo inventore veritatis et quasi architecto beatae vitae dicta sunt explicabo.</p>
    </div>
    <a class="btn btn-blue" href="#" style="left:646px;top:1322px;width:156px;height:37px">Read More</a>
  </section>

  <section class="services abs">
    <svg class="abs" style="left:0;top:0" width="1200" height="140" viewBox="0 0 1200 140" preserveAspectRatio="none">
      <path d="M0 0 H1200 V10 Q600 170 0 10Z" fill="#fff"/>
      <path d="M0 30 Q600 170 1200 30" fill="none" stroke="#fff" stroke-width="3"/>
    </svg>
    <h2 class="section-title services-title abs center">What We Do</h2>
    <p class="services-intro abs center">Lorem ipsum dolor sit amet, consectetur adipiscing elit, sed do eiusmod tempor incididunt ut labore et dolore magna aliqua. Quis ipsum suspendisse ultrices gravida. Risus commodo viverra maecenas accumsan lacus vel facilisis.</p>

    <div class="card-photo" style="left:112px;top:571px;width:317px;height:212px;background:linear-gradient(180deg,#9fc9e6,#a8b7a2 45%,#8fd0ec 75%,#5fb7e3)" role="img" aria-label="Worker standing in an empty swimming pool beside a house"></div>
    <div class="card-num center" style="left:112px;top:792px">01</div>
    <h3 class="card-title center" style="left:112px;top:850px">Swimming Pool Services</h3>
    <p class="card-text center" style="left:140px;top:890px">Excepteur sint occaecat cupidatat non proident, sunt in culpa qui officia deserunt mollit anim id est laborum.</p>
    <a class="btn btn-white" href="#" style="left:193px;top:989px;width:154px;height:37px">Read More</a>

    <div class="feature-card abs">
      <div class="abs center" style="top:30px;width:318px;font-size:40px;color:var(--blue)">02</div>
      <h3 class="abs center" style="top:90px;width:318px;font-family:var(--serif);font-weight:700;font-size:24px;color:#5a5a5a">Pool Cleaning Service</h3>
      <p class="abs center" style="left:29px;top:130px;width:260px;font-size:14px;line-height:25px;color:#666">Excepteur sint occaecat cupidatat non proident, sunt in culpa qui officia deserunt mollit anim id est laborum.</p>
      <a class="btn btn-blue" href="#" style="left:82px;top:236px;width:154px;height:37px">Read More</a>
      <div class="photo" style="left:4px;top:304px;width:310px;height:210px;background:linear-gradient(160deg,#6cc3ea,#2f8fd2 60%,#1d6fc0)" role="img" aria-label="Pool vacuum head sweeping a pool floor"></div>
    </div>

    <div class="card-photo" style="left:770px;top:571px;width:317px;height:212px;background:linear-gradient(120deg,#3a7ea8,#6aa7c2 45%,#d9e4ea)" role="img" aria-label="Technician scrubbing tiles on a pool wall"></div>
    <div class="card-num center" style="left:770px;top:792px">03</div>
    <h3 class="card-title center" style="left:770px;top:850px">Swimming Pool Repair</h3>
    <p class="card-text center" style="left:798px;top:890px">Excepteur sint occaecat cupidatat non proident, sunt in culpa qui officia deserunt mollit anim id est laborum.</p>
    <a class="btn btn-white" href="#" style="left:851px;top:989px;width:154px;height:37px">Read More</a>
  </section>

  <section class="why abs">
    <h2 class="section-title why-title abs center">Why Choose Us</h2>
    <div class="why-item center" style="left:102px">
      <svg width="80" height="80" viewBox="0 0 80 80" fill="none" stroke="#fff" stroke-width="2.5"><circle cx="40" cy="30" r="16"/><path d="M33 30l5 5 9-10"/><path d="M10 60h14l12 6h18l12-10"/><path d="M10 70h14"/></svg>
      <h3>Quality Services</h3>
      <p>Duis aute irure dolor in derit voluptate velit esse cillum dolore eu fugiat nulla pariatur.</p>
    </div>
    <div class="why-item center" style="left:353px">
      <svg width="80" height="80" viewBox="0 0 80 80" fill="none" stroke="#fff" stroke-width="2.5"><circle cx="40" cy="30" r="7"/><circle cx="22" cy="40" r="6"/><circle cx="58" cy="40" r="6"/><path d="M28 56c0-8 24-8 24 0v10H28z"/><path d="M12 66c0-10 18-10 18 0"/><path d="M50 66c0-10 18-10 18 0"/><path d="M40 10l2 4 4 1-3 3 1 4-4-2-4 2 1-4-3-3 4-1z"/></svg>
      <h3>Experienced Team</h3>
      <p>Duis aute irure dolor in derit voluptate velit esse cillum dolore eu fugiat nulla pariatur.</p>
    </div>
    <div class="why-item center" style="left:605px">
      <svg width="80" height="80" viewBox="0 0 80 80" fill="none" stroke="#fff" stroke-width="2.5"><circle cx="44" cy="24" r="14"/><path d="M44 16v16M40 20h7a3 3 0 0 1 0 5h-6a3 3 0 0 0 0 5h7"/><path d="M10 62h14l12 6h18l12-12"/><path d="M24 54h16"/></svg>
      <h3>Affordable Pricing</h3>
      <p>Duis aute irure dolor in derit voluptate velit esse cillum dolore eu fugiat nulla pariatur.</p>
    </div>
    <div class="why-item center" style="left:856px">
      <svg width="80" height="80" viewBox="0 0 80 80" fill="none" stroke="#fff" stroke-width="2.5"><path d="M16 36l24-10 24 10v26L40 72 16 62z"/><path d="M16 36l24 10 24-10M40 46v26"/><circle cx="40" cy="36" r="8"/><path d="M36 36l3 3 5-6"/><path d="M40 6v8M26 12l4 6M54 12l-4 6"/></svg>
      <h3>Quality Product</h3>
      <p>Duis aute irure dolor in derit voluptate velit esse cillum dolore eu fugiat nulla pariatur.</p>
    </div>
  </section>

  <section class="blog">
    <h2 class="section-title blog-title abs center">Our Blog</h2>
    <div class="arrow"><svg width="42" height="42" viewBox="0 0 42 42"><path d="M24 13l-8 8 8 8" fill="none" stroke="#fff" stroke-width="4"/></svg></div>
    <div class="arrow" style="left:1110px"><svg width="42" height="42" viewBox="0 0 42 42"><path d="M18 13l8 8-8 8" fill="none" stroke="#fff" stroke-width="4"/></svg></div>
    <div class="arrow" style="left:47px"><svg width="42" height="42" viewBox="0 0 42 42"><path d="M24 13l-8 8 8 8" fill="none" stroke="#fff" stroke-width="4"/></svg></div>

    <article class="blog-card center" style="left:112px">
      <div class="blog-photo" role="img" aria-label="Technician servicing a backyard pool lined with trees" style="background:linear-gradient(180deg,#c9dcea,#3f6a3c 35%,#2f9ad8 60%,#1f7dc6)"></div>
      <div class="blog-date">14-March-2024</div>
      <h3>Lorem ipsum dolor sit</h3>
      <p>Nemo enim ipsam voluptatem aut odit consequuntur magni dolores eos qui ratione voluptatem sequi nesciunt.</p>
      <a href="#">Read More....</a>
    </article>
    <article class="blog-card center" style="left:447px">
      <div class="blog-photo" role="img" aria-label="Worker brushing the floor of a drained tiled pool" style="background:linear-gradient(160deg,#cfe6f4,#8fc7ea 50%,#6cb2e2)"></div>
      <div class="blog-date">14-March-2024</div>
      <h3>Lorem ipsum dolor sit</h3>
      <p>Nemo enim ipsam voluptatem aut odit consequuntur magni dolores eos qui ratione voluptatem sequi nesciunt.</p>
      <a href="#">Read More....</a>
    </article>
    <article class="blog-card center" style="left:780px">
      <div class="blog-photo" role="img" aria-label="Pool cleaning pole reaching into turquoise water from the deck" style="background:linear-gradient(110deg,#1a8a8c,#2aa3a6 55%,#c7a98a 75%,#b59677)"></div>
      <div class="blog-date">14-March-2024</div>
      <h3>Lorem ipsum dolor sit</h3>
      <p>Nemo enim ipsam voluptatem aut odit consequuntur magni dolores eos qui ratione voluptatem sequi nesciunt.</p>
      <a href="#">Read More....</a>
    </article>
  </section>

  <footer class="footer abs">
    <svg class="abs" style="left:0;top:0" width="1200" height="140" viewBox="0 0 1200 140" preserveAspectRatio="none">
      <path d="M0 0 H1200 V20 Q600 170 0 0Z" fill="#fff"/>
      <path d="M0 10 Q600 190 1200 30" fill="none" stroke="var(--blue)" stroke-width="6"/>
    </svg>
    <h2 class="section-title contact-title abs center">Contact Us</h2>
    <div class="field" style="left:112px;top:368px">Name</div>
    <div class="field" style="left:612px;top:368px">Phone</div>
    <div class="field" style="left:112px;top:447px">Email</div>
    <div class="field" style="left:612px;top:447px">Message</div>
    <a class="btn btn-blue" href="#" style="left:522px;top:533px;width:154px;height:37px;font-weight:400">Submit</a>

    <div class="foot-brand abs">Coral Basin<br>Pool Service</div>
    <div class="foot-info" style="top:765px">
      <svg width="16" height="16" viewBox="0 0 16 16"><path d="M4 1c1 0 1.5.5 2 1.5l1 2c.4 1 0 1.5-.6 2l-.6.5c.7 1.5 2 2.8 3.5 3.5l.5-.6c.5-.6 1-1 2-.6l2 1c1 .5 1.5 1 1.5 2-1 2.5-4 3-7 1S2 8 1.5 5C1.5 3 2.5 1 4 1z" fill="var(--blue)"/></svg>
      <span>+ 1 888 888 8888</span>
    </div>
    <div class="foot-info" style="top:806px">
      <svg width="16" height="20" viewBox="0 0 16 20"><path d="M8 0a7 7 0 0 1 7 7c0 5-7 13-7 13S1 12 1 7a7 7 0 0 1 7-7z" fill="var(--blue)"/><circle cx="8" cy="7" r="2.5" fill="var(--night)"/></svg>
      <span>123,Coral Basin Pool Service Company<br>NA,123456</span>
    </div>
    <div class="foot-info" style="top:866px">
      <svg width="16" height="14" viewBox="0 0 16 14"><rect x="0" y="1" width="16" height="12" rx="1" fill="var(--blue)"/><path d="M0 2l8 6 8-6" fill="none" stroke="var(--night)" stroke-width="1.5"/></svg>
      <span>Info@Coral Basin Pool Service.com</span>
    </div>

    <div class="foot-col" style="left:515px">
      <h4>Quick Links</h4>
      <a href="#">Home</a><a href="#">About Us</a><a href="#">Services</a><a href="#">Blog</a><a href="#">Contact Us</a>
    </div>
    <div class="foot-col" style="left:744px">
      <h4>Other Links</h4>
      <a href="#">Privacy Policy</a><a href="#">Terms of Service</a><a href="#">Disclaimer</a><a href="#">Help</a><a href="#">Faq</a>
    </div>
    <div class="foot-col" style="left:976px">
      <h4>Follow Us</h4>
      <a href="#">Snapwave</a><a href="#">Chirpline</a><a href="#">Reelhub</a><a href="#">Worknet</a>
    </div>
    <div class="copyright abs center">Copyright © 2024 Coral Basin Pool Service. All Right Reserved</div>
  </footer>

</div>
</body>
</html>
```